Label for luxury drink/cocktail flavour bags

I need a luxury label designed for our new product, which are infusion bags for drinks and cocktails. We are a saffron producer so all will contain saffron and the name of the product is Velvet Steeps. There will be 10 bags in each pack, and the packaging will be a cardboard cylinder which is 105mm high x 85mm wide. The tagline is "Elevate every pour", and the first variety will be called Lunar Orchard. The ingredients are saffron, rose petals and hibiscus flower. The label needs to feel luxurious, and I would like a gold foil element in the final printing so please include that in the design. Our brand is Kestrel Valley Saffron. I like clean designs, without excessive detail but would be open to some saffron flower illustrations included. The design needs to be editable for different blends as we release them.

Target Market(s)

30-60 year old females with a high income

Industry/Entity Type

Food and drink

Requirements
Must have
• Elevate every pour, Brand, Ingredients section (for this one, Saffron, Rose Petals, Hibiscus Flowers), and one of the attached "made in" marks on the pack

```html
<!DOCTYPE html>
<html lang="en">
<head>
<meta charset="utf-8">
<title>Velvet Steeps – Lunar Orchard Label</title>
<link rel="stylesheet" href="https://fonts.googleapis.com/css2?family=Montserrat:wght@400;500;600&display=swap">
<style>
  :root {
    --page: #ffffff;
    --label-bg: #ffffff;
    --ink: #111111;
    --ink-soft: #1c1c1c;
    --frame: #1a1a1a;
    --illustration: #ececec;
    --illustration-fade: rgba(236, 236, 236, 0);
    --badge-edge: #1f8a5a;
    --badge-fill: #f4faf6;
  }
  * { box-sizing: border-box; margin: 0; padding: 0; }
  html, body {
    width: 1200px;
    height: 1200px;
    overflow: hidden;
    background: var(--page);
    font-family: "Montserrat", sans-serif;
    color: var(--ink);
  }
  .canvas {
    position: relative;
    width: 1200px;
    height: 1200px;
  }
  .label {
    position: absolute;
    left: 80px;
    top: 179px;
    width: 975px;
    height: 789px;
    transform: scale(1.0667);
    transform-origin: top left;
    background: var(--label-bg);
    border: 2px solid var(--frame);
  }
  .front-panel {
    position: absolute;
    left: 0;
    top: 0;
    width: 652px;
    height: 100%;
  }
  .flower-art {
    position: absolute;
    left: 100px;
    top: 242px;
    width: 400px;
    height: 545px;
    background: radial-gradient(ellipse at 55% 35%, var(--illustration) 0%, var(--illustration) 35%, var(--illustration-fade) 72%);
  }
  .centered {
    position: absolute;
    left: 0;
    width: 652px;
    text-align: center;
  }
  .brand-name {
    top: 112px;
    font-weight: 600;
    font-size: 17px;
    letter-spacing: 0.32em;
    text-transform: uppercase;
    color: var(--ink);
  }
  .product-name {
    top: 250px;
    font-weight: 600;
    font-size: 60px;
    line-height: 60px;
    letter-spacing: 0.08em;
    text-transform: uppercase;
    color: var(--ink);
  }
  .tagline {
    top: 389px;
    font-weight: 500;
    font-size: 20px;
    letter-spacing: 0.26em;
    text-transform: uppercase;
    color: var(--ink-soft);
  }
  .variety {
    top: 539px;
    font-weight: 600;
    font-size: 32px;
    letter-spacing: 0.2em;
    text-transform: uppercase;
  }
  .pack-count {
    top: 728px;
    font-weight: 600;
    font-size: 32px;
    letter-spacing: 0.16em;
    text-transform: uppercase;
  }
  .info-panel {
    position: absolute;
    left: 650px;
    top: 0;
    width: 252px;
    height: 100%;
    text-align: center;
  }
  .ingredients-title {
    position: absolute;
    top: 155px;
    width: 100%;
    font-weight: 400;
    font-size: 28px;
  }
  .ingredients-list,
  .description {
    position: absolute;
    width: 100%;
    font-weight: 400;
    font-size: 19px;
    line-height: 23px;
  }
  .ingredients-list { top: 207px; }
  .divider {
    position: absolute;
    top: 348px;
    left: 78px;
    width: 96px;
    height: 3px;
    background: var(--ink);
  }
  .description { top: 388px; }
  .origin-badge {
    position: absolute;
    left: 20px;
    top: 585px;
    width: 213px;
    height: 57px;
    border: 2px solid var(--badge-edge);
    border-radius: 3px;
    background: var(--badge-fill);
  }
</style>
</head>
<body>
  <main class="canvas">
    <section class="label">
      <div class="front-panel">
        <div class="flower-art" role="img" aria-label="Faint line illustration of a saffron crocus flower with long leaves"></div>
        <div class="centered brand-name">Kestrel Valley Saffron</div>
        <h1 class="centered product-name">Velvet<br>Steeps</h1>
        <p class="centered tagline">Elevate every pour</p>
        <h2 class="centered variety">Lunar Orchard</h2>
        <p class="centered pack-count">10 Bags</p>
      </div>
      <aside class="info-panel">
        <h3 class="ingredients-title">Ingredients</h3>
        <p class="ingredients-list">Saffron, Rose Petals,<br>Hibiscus Flowers</p>
        <div class="divider"></div>
        <p class="description">Lorem ipsum dolor<br>sit amet, consec-<br>tetuer adipiscing<br>elit, sed diam</p>
        <div class="origin-badge" role="img" aria-label="Country of origin mark"></div>
      </aside>
    </section>
  </main>
</body>
</html>
```